Letterhead for Law Firm - Logo already prepared

I previously used to prepare a logo which I was quite pleased with, a copy is attached for your reference. I would like the font of the logo to be all the same size, rather than the 'S' and 'L' being larger than the other letters.
I have copies of the attached in other formats if necessary.
I need a letterhead prepared which is virtually identical to the draft attached, however I will be adding an address, phone number, fax number, mobile number and email. I will provide these details with whoever can assist me.
I will also be providing insurance details to be listed at the foot of the page.
Finally, I need the file to be supplied as a high resolution pdf with 2mm bleed.
If you require any further information, please do not hesitate to contact me.

```html
<!DOCTYPE html>
<html lang="en">
<head>
<meta charset="utf-8">
<title>Marlowe Legal – Letterhead</title>
<link rel="stylesheet" href="https://fonts.googleapis.com/css2?family=Cinzel:wght@500&family=Questrial&display=swap">
<style>
  :root {
    --paper: #ffffff;
    --bubble-tone: #f3f3f3;
    --bubble-soft: #fafafa;
    --accent: #f26a21;
    --ink-dark: #2f2f2f;
    --ink-footer: #4a4a4a;
    --divider-grey: #9a9a9a;
  }
  html, body {
    margin: 0;
    padding: 0;
    width: 906px;
    height: 1200px;
    overflow: hidden;
    background: var(--paper);
  }
  .letterhead {
    position: relative;
    width: 906px;
    height: 1200px;
    background: var(--paper);
    overflow: hidden;
  }
  .background-texture {
    position: absolute;
    left: 0;
    top: 0;
    width: 906px;
    height: 1150px;
    background:
      radial-gradient(ellipse at 30% 25%, var(--bubble-tone) 0%, transparent 60%),
      radial-gradient(ellipse at 75% 65%, var(--bubble-tone) 0%, transparent 60%),
      linear-gradient(180deg, var(--bubble-soft) 0%, var(--paper) 100%);
  }
  .brand {
    position: absolute;
    top: 20px;
    right: 16px;
    display: flex;
    align-items: center;
    gap: 14px;
  }
  .brand-mark {
    width: 76px;
    height: 76px;
    border-radius: 50%;
    background: var(--accent);
  }
  .brand-name {
    font-family: "Cinzel", serif;
    font-weight: 500;
    font-size: 32px;
    letter-spacing: 0.5px;
    color: var(--ink-dark);
    margin: 0;
  }
  .contact-footer {
    position: absolute;
    left: 12px;
    bottom: 18px;
    font-family: "Questrial", sans-serif;
    font-size: 18.5px;
    color: var(--ink-footer);
    white-space: nowrap;
    display: flex;
    align-items: center;
  }
  .contact-footer .divider {
    display: inline-block;
    width: 1.5px;
    height: 21px;
    margin: 0 9px 0 5px;
    background: var(--divider-grey);
  }
  .contact-footer .divider--accent {
    width: 2.5px;
    background: var(--accent);
  }
</style>
</head>
<body>
  <main class="letterhead">
    <div class="background-texture" role="img" aria-label="Faint pale grey bubble pattern covering the page"></div>

    <header class="brand">
      <span class="brand-mark"></span>
      <h1 class="brand-name">Marlowe Legal</h1>
    </header>

    <footer class="contact-footer">
      <span class="contact-address">Address Text here, Address Text here</span>
      <span class="divider"></span>
      <span class="contact-phone">Phone ; 000-001-3309</span>
      <span class="divider divider--accent"></span>
      <span class="contact-web">Web : www.websitelink.com</span>
    </footer>
  </main>
</body>
</html>
```